Veltrona Services

Double sided business cards with color on front and black and white on back. I have basic ideas and graphics, but am looking for someone to take them to the next level

```html
<!DOCTYPE html>
<html lang="en">
<head>
<meta charset="utf-8">
<title>Veltrona Services – Business Card</title>
<link href="https://fonts.googleapis.com/css2?family=Montserrat:wght@400;500;700&family=Roboto:wght@700&display=swap" rel="stylesheet">
<style>
  :root{
    --page:#ececec;
    --paper:#ffffff;
    --ink:#111111;
    --black:#000000;
    --red:#e0262e;
    --blue:#3b8fd0;
    --mark:#eef0f6;
    --text:#1a1a1a;
  }
  *{box-sizing:border-box;margin:0;padding:0}
  html,body{width:687px;height:1200px;overflow:hidden}
  body{background:var(--page);font-family:"Montserrat",sans-serif;position:relative}
  .card{position:absolute;left:63px;width:560px;height:320px;background:var(--paper);
        box-shadow:0 2px 8px rgba(0,0,0,.25);overflow:hidden}
  .card--front{top:260px}
  .card--back{top:620px}
  .card svg.art{position:absolute;inset:0;width:560px;height:320px}
  .brand-mark{position:absolute;left:200px;top:30px;width:160px;height:160px;border-radius:50%;background:var(--mark)}
  .brand-name{position:absolute;left:0;right:0;top:196px;text-align:center;
        font-family:"Roboto",sans-serif;font-weight:700;font-size:20px;color:var(--red);letter-spacing:.3px}
  .site-url{position:absolute;left:0;right:0;top:284px;text-align:center;color:#fff;
        font-weight:700;font-size:16px;letter-spacing:2.4px}
  .person{position:absolute;left:32px;top:16px}
  .person-name{font-family:"Roboto",sans-serif;font-weight:700;font-size:24px;line-height:1}
  .person-name .first{color:var(--red)}
  .person-name .last{color:var(--blue)}
  .person-role{font-size:14px;letter-spacing:1.2px;color:var(--text);margin-top:4px}
  .rule{width:144px;height:2px;background:var(--ink);margin-top:4px}
  .contacts{position:absolute;left:30px;top:90px;list-style:none}
  .contact{display:flex;align-items:center;gap:9px;font-size:13.5px;line-height:17px;color:var(--text);font-weight:500}
  .contact + .contact{margin-top:11px}
  .contact svg{width:24px;height:24px;flex:none}
  .emblem{position:absolute;left:359px;top:74px;width:172px;height:172px;border-radius:50%;
        background:#fff;display:flex;align-items:center;justify-content:center}
  .emblem span{font-family:"Montserrat",sans-serif;font-weight:700;font-size:20px;color:var(--black);letter-spacing:1px}
</style>
</head>
<body>

<section class="card card--front" aria-label="Card front">
  <svg class="art" viewBox="0 0 560 320" aria-hidden="true">
    <defs>
      <linearGradient id="front-spectrum" x1="0" y1="0" x2="1" y2="0">
        <stop offset="0" stop-color="#5a55c8"/>
        <stop offset=".18" stop-color="#45a6d6"/>
        <stop offset=".35" stop-color="#7cc456"/>
        <stop offset=".5" stop-color="#e0304a"/>
        <stop offset=".75" stop-color="#c1408e"/>
        <stop offset="1" stop-color="#f0dc1a"/>
      </linearGradient>
    </defs>
    <path d="M0,180 Q280,326 560,180 L560,248 Q280,297 0,248 Z" fill="url(#front-spectrum)"/>
    <path d="M0,248 Q280,297 560,248 L560,320 L0,320 Z" fill="#000"/>
    <g class="dots-left" fill="#7cc456">
      <circle cx="32" cy="53" r="7" opacity=".15"/>
      <circle cx="32" cy="79" r="4"/>
      <circle cx="29" cy="119" r="6"/>
      <circle cx="14" cy="129" r="4" opacity=".8"/>
      <circle cx="47" cy="135" r="6" opacity=".8"/>
      <circle cx="60" cy="155" r="10" opacity=".12"/>
      <circle cx="48" cy="110" r="2.5"/>
      <circle cx="61" cy="110" r="4" opacity=".2"/>
    </g>
    <g class="dots-right">
      <circle cx="525" cy="53" r="7" fill="#d04aa8" opacity=".15"/>
      <circle cx="525" cy="79" r="4" fill="#d04aa8"/>
      <circle cx="523" cy="96" r="2.5" fill="#e0262e"/>
      <circle cx="528" cy="119" r="6" fill="#d04aa8"/>
      <circle cx="510" cy="135" r="6" fill="#e0262e"/>
      <circle cx="543" cy="129" r="4" fill="#e0262e"/>
      <circle cx="497" cy="155" r="10" fill="#e0262e" opacity=".12"/>
      <circle cx="507" cy="110" r="2.5" fill="#c1408e"/>
    </g>
  </svg>
  <div class="brand-mark" aria-hidden="true"></div>
  <p class="brand-name">VELTRONA SERVICES</p>
  <p class="site-url">www.veltronaservices.com</p>
</section>

<section class="card card--back" aria-label="Card back">
  <svg class="art" viewBox="0 0 560 320" aria-hidden="true">
    <defs>
      <linearGradient id="back-spectrum" x1="0" y1="0" x2="0" y2="1">
        <stop offset="0" stop-color="#5a55c8"/>
        <stop offset=".25" stop-color="#8c8ae8"/>
        <stop offset=".5" stop-color="#1f6f92"/>
        <stop offset=".8" stop-color="#66c07a"/>
        <stop offset="1" stop-color="#a8ea8a"/>
      </linearGradient>
    </defs>
    <path d="M350,0 L560,0 L560,320 L268,320 C300,260 335,150 350,0 Z" fill="#000"/>
    <path d="M324,0 L350,0 C335,150 300,260 268,320 L110,320 C220,260 300,150 324,0 Z" fill="url(#back-spectrum)"/>
    <g class="dots">
      <circle cx="240" cy="218" r="2.5" fill="#f0dc1a"/>
      <circle cx="217" cy="241" r="6" fill="#f0dc1a"/>
      <circle cx="233" cy="233" r="5" fill="#c9c4ee" opacity=".5"/>
      <circle cx="212" cy="259" r="2.5" fill="#5a55c8"/>
      <circle cx="223" cy="261" r="2.5" fill="#3b8fd0"/>
      <circle cx="171" cy="269" r="11" fill="#c9c4ee" opacity=".35"/>
      <circle cx="171" cy="285" r="2.5" fill="#f0a01a"/>
      <circle cx="187" cy="287" r="6" fill="#5a55c8"/>
      <circle cx="97" cy="288" r="6" fill="#5a55c8"/>
      <circle cx="69" cy="293" r="2.5" fill="#5a55c8"/>
      <circle cx="78" cy="300" r="2.5" fill="#3b8fd0"/>
      <circle cx="32" cy="299" r="6" fill="#3b8fd0"/>
      <circle cx="51" cy="309" r="4" fill="#5a55c8"/>
      <circle cx="12" cy="294" r="11" fill="#c9dcf2" opacity=".5"/>
      <circle cx="13" cy="313" r="2.5" fill="#3b8fd0"/>
    </g>
  </svg>

  <div class="person">
    <p class="person-name"><span class="first">DARA</span> <span class="last">QUILL</span></p>
    <p class="person-role">DIRECTOR</p>
    <div class="rule"></div>
  </div>

  <ul class="contacts">
    <li class="contact">
      <svg viewBox="0 0 24 24" aria-hidden="true"><circle cx="12" cy="12" r="11" fill="none" stroke="#3a3a9a" stroke-width="1.6"/><circle cx="12" cy="12" r="8.5" fill="none" stroke="#7cc456" stroke-width="1"/><path d="M8.5,7.5 l2,0 l1,2.5 l-1.3,1 a6,6 0 0 0 2.8,2.8 l1-1.3 l2.5,1 l0,2 a1,1 0 0 1 -1,1 a9,9 0 0 1 -8-8 a1,1 0 0 1 1-1z" fill="#3a3a9a"/></svg>
      <span>852 0140 5521</span>
    </li>
    <li class="contact">
      <svg viewBox="0 0 24 24" aria-hidden="true"><circle cx="12" cy="12" r="11" fill="none" stroke="#3a3a9a" stroke-width="1.6"/><circle cx="12" cy="12" r="8.5" fill="none" stroke="#7cc456" stroke-width="1"/><path d="M12,6 a4,4 0 0 1 4,4 c0,3 -4,7.5 -4,7.5 c0,0 -4,-4.5 -4,-7.5 a4,4 0 0 1 4,-4z" fill="#3a3a9a"/><circle cx="12" cy="10" r="1.5" fill="#fff"/></svg>
      <span>Harbor Civic Hall<br>Main 04417 - UK</span>
    </li>
    <li class="contact">
      <svg viewBox="0 0 24 24" aria-hidden="true"><circle cx="12" cy="12" r="11" fill="none" stroke="#3a3a9a" stroke-width="1.6"/><circle cx="12" cy="12" r="8.5" fill="none" stroke="#7cc456" stroke-width="1"/><rect x="7" y="8.5" width="10" height="7" fill="#3a3a9a"/><path d="M7,8.5 L12,12.5 L17,8.5" fill="none" stroke="#fff" stroke-width="1"/></svg>
      <span>hello@veltrona.com</span>
    </li>
    <li class="contact">
      <svg viewBox="0 0 24 24" aria-hidden="true"><circle cx="12" cy="12" r="11" fill="none" stroke="#3a3a9a" stroke-width="1.6"/><circle cx="12" cy="12" r="8.5" fill="none" stroke="#7cc456" stroke-width="1"/><circle cx="12" cy="12" r="5" fill="none" stroke="#3a3a9a" stroke-width="1.2"/><path d="M7,12 h10 M12,7 v10 M12,7 c-2.5,2.5 -2.5,7.5 0,10 M12,7 c2.5,2.5 2.5,7.5 0,10" fill="none" stroke="#3a3a9a" stroke-width="0.9"/></svg>
      <span>www.veltrona.net</span>
    </li>
  </ul>

  <div class="emblem"><span>VELTRONA</span></div>
</section>

</body>
</html>
```